Forget what you know about corporate well

I need a one-page flies used for print, to embedding in a website, all social media platforms and email.

Target Market(s)

Business

Industry/Entity Type

Health And Wellness

Font styles to use
Serif
Script
Other font styles liked:
• I would like the designers opinion on the font

Colors

Designer to choose colors to be used in the design.

Requirements
Must have
• This is the wording:
• Did you know that 75% of healthcare costs are incurred by preventable diseases? Cardiovascular disease, cancer, and diabetes are the three major causes of rising health care plans and are all preventable.
• Milo and his team have spent decades learning how to increase productivity, reduce absenteeism, and increase employee engagement, all leading to lowering healthcare costs. Together, they have developed a system created to target the masses all while addressing individual needs. Their corporate training challenges helps to engrain positive habits through a carefully curated accountability and reward system.
• How it works:
• Step 1 – evaluate the needs of your business;
• Step 2 – set up individualized workshops based on highest needs;
• Step 3 – create a customized corporate training challenge.
• Why Milo?
• Milo excels at motivational speaking. He is an author, a nutritionist and a professional athlete with a master’s degree in clinical nutrition. He is a teacher of corporate wellness at Fernhollow College and a health coach. Milo has been featured in national magazines, podcasts, and popular fitness websites. Milo’s own health issues put him on a quest to heal himself and others. With twenty-five years of experience and a passion for wellness, he can provide your company with an unforgettable experience.
Nice to have
• I will not give my opinion, I believe that is an insult to the designer. All of the verbiage is above and I attached a plethora of pictures.
Should not have
• No opinion

```html
<!DOCTYPE html>
<html lang="en">
<head>
<meta charset="utf-8">
<title>Brightpath Wellness – Corporate Wellness Flyer</title>
<link href="https://fonts.googleapis.com/css2?family=Roboto:wght@400;500&family=Roboto+Condensed:wght@700&display=swap" rel="stylesheet">
<style>
  :root {
    --slate: #3d4455;
    --slate-deep: #2b3140;
    --lime: #7ed400;
    --lime-soft: #c7ee8f;
    --green-text: #1a9a3c;
    --cream: #fbfbf0;
    --ink: #1f1f1f;
  }
  * { margin: 0; padding: 0; box-sizing: border-box; }
  html, body { width: 927px; height: 1200px; overflow: hidden; background: var(--cream); }
  .flyer {
    position: relative; width: 927px; height: 1200px; overflow: hidden;
    background: var(--cream);
    font-family: "Roboto", Arial, sans-serif; color: var(--ink);
  }
  .backdrop { position: absolute; inset: 0; }
  .brand-mark {
    position: absolute; left: 366px; top: 70px; width: 228px; height: 228px;
    border-radius: 50%; background: #fff;
    display: flex; flex-direction: column; align-items: center; justify-content: center;
    text-align: center;
  }
  .brand-name {
    font-family: "Roboto", Arial, sans-serif; font-weight: 500;
    font-size: 17px; line-height: 1.35; color: var(--slate);
  }
  .section { position: absolute; left: 60px; width: 807px; text-align: center; }
  .heading {
    font-family: "Roboto Condensed", "Arial Narrow", sans-serif; font-weight: 700;
    color: var(--green-text); font-size: 26px; line-height: 32px;
  }
  .body-copy { font-size: 16px; line-height: 21.7px; font-weight: 500; }
  .intro { top: 383px; }
  .how { top: 600px; }
  .how .body-copy { line-height: 21.5px; font-weight: 400; }
  .step-label { color: var(--green-text); font-weight: 500; }
  .why { top: 960px; }
  .why .body-copy { font-weight: 400; }
  .photo {
    position: absolute; box-shadow: 0 3px 8px rgba(0,0,0,.45);
  }
  .photo-brick { left: 50px; top: 723px; width: 256px; height: 170px;
    background: linear-gradient(135deg, #b0573f, #8e3f2c 60%, #6c3124); }
  .photo-office { left: 341px; top: 729px; width: 246px; height: 164px;
    background: linear-gradient(135deg, #d9dde0, #c4c9cd 55%, #8e2b2f 100%); }
  .photo-talk { left: 622px; top: 723px; width: 255px; height: 170px;
    background: linear-gradient(160deg, #5a5e62, #2e3236 55%, #8a7a6a); }
</style>
</head>
<body>
<main class="flyer">
  <svg class="backdrop" width="927" height="1200" viewBox="0 0 927 1200" aria-hidden="true">
    <defs>
      <linearGradient id="sheen" x1="0" y1="0" x2="1" y2="1">
        <stop offset="0" stop-color="#ffffff" stop-opacity=".9"/>
        <stop offset="1" stop-color="#e9ebe2" stop-opacity="0"/>
      </linearGradient>
    </defs>
    <!-- top corner shapes -->
    <polygon points="0,0 927,0 927,130 520,150 0,262" fill="var(--slate)"/>
    <polygon points="560,0 927,0 927,60 640,105 540,90" fill="var(--lime)"/>
    <polygon points="0,150 420,120 0,262" fill="url(#sheen)" opacity=".25"/>
    <polygon points="540,140 927,90 927,250 760,175" fill="url(#sheen)" opacity=".35"/>
    <!-- circular frame -->
    <path d="M262,182 A222,222 0 0 1 560,-22" fill="none" stroke="var(--lime)" stroke-width="3"/>
    <path d="M640,12 A222,222 0 0 1 580,380" fill="none" stroke="var(--lime)" stroke-width="3"/>
    <circle cx="480" cy="184" r="180" fill="var(--cream)"/>
    <path d="M336,120 A160,160 0 0 1 580,50 L560,110 A110,110 0 0 0 380,140 Z" fill="var(--lime-soft)"/>
    <circle cx="480" cy="184" r="138" fill="var(--slate)"/>
    <circle cx="480" cy="184" r="114" fill="#fff"/>
    <!-- photo band -->
    <rect x="0" y="702" width="927" height="226" fill="var(--slate)"/>
    <polygon points="300,760 520,702 700,702 340,800" fill="var(--lime)"/>
    <polygon points="640,702 927,702 927,712 620,730" fill="var(--lime)"/>
    <polygon points="840,900 927,860 927,928 870,928" fill="var(--lime)"/>
    <polygon points="0,702 80,702 0,760" fill="var(--slate-deep)"/>
    <!-- bottom corner shapes -->
    <polygon points="0,1060 420,1200 0,1200" fill="var(--slate)" opacity=".9"/>
    <polygon points="0,1140 600,1200 0,1200" fill="var(--lime)"/>
    <polygon points="860,1180 927,1160 927,1200 840,1200" fill="var(--slate)" opacity=".5"/>
  </svg>

  <div class="brand-mark">
    <p class="brand-name">Brightpath Wellness<br>Milo T. Varden</p>
  </div>

  <section class="section intro">
    <h1 class="heading">Did you know that 75% of healthcare costs<br>are incurred by preventable diseases?</h1>
    <p class="body-copy">Cardiovascular disease, cancer, and diabetes are the three major causes of rising health care plans and are all preventable. Milo and his team have spent decades learning how to increase productivity, reduce absenteeism, and increase employee engagement, all leading to lowering healthcare costs. Together, they have developed a system created to target the masses all while addressing individual needs. Their corporate training challenges helps to engrain positive habits through a carefully curated accountability and reward system.</p>
  </section>

  <section class="section how">
    <h2 class="heading">How it works:</h2>
    <p class="body-copy"><span class="step-label">Step 1</span> – evaluate the needs of your business;<br>
    <span class="step-label">Step 2</span> – set up individualized workshops based on highest needs;<br>
    <span class="step-label">Step 3</span> – create a customized corporate training challenge.</p>
  </section>

  <div class="photo photo-brick" role="img" aria-label="Portrait of Milo smiling in front of a brick wall"></div>
  <div class="photo photo-office" role="img" aria-label="Portrait of Milo in a red polo shirt in a bright office"></div>
  <div class="photo photo-talk" role="img" aria-label="Milo giving a wellness talk to a seated audience"></div>

  <section class="section why">
    <h2 class="heading">Why Milo?</h2>
    <p class="body-copy">Milo excels at motivational speaking. He is an author, a nutritionist and a professional athlete with a master’s degree in clinical nutrition. He is a teacher of corporate wellness at Fernhollow College and a health coach. Milo has been featured in national magazines, podcasts, and popular fitness websites. Milo’s own health issues put him on a quest to heal himself and others. With twenty-five years of experience and a passion for wellness, he can provide your company with an unforgettable experience.</p>
  </section>
</main>
</body>
</html>
```